Saltmarsh Valley Lending Flyer

I would like our main long logo with the bird and words Saltmarsh Valley Lending with pictures of what we finance along the bottom.
Car , 4x4 , boat, excavator , Cash Loans and houses
Needs to look good on leaflet and large signage.
Simple but cool looking so it stands out.

```html
<!DOCTYPE html>
<html lang="en">
<head>
<meta charset="utf-8">
<title>Saltmarsh Valley Lending Flyer</title>
<link rel="stylesheet" href="https://fonts.googleapis.com/css2?family=Oswald:wght@500;700&family=Open+Sans:wght@400;600;700&display=swap">
<style>
  :root {
    --orange: #f07f1b;
    --orange-dark: #d9660a;
    --charcoal: #2b2b2d;
    --charcoal-deep: #1d1d1f;
    --grey-text: #5a5a5c;
    --light: #ffffff;
    --rule: #d8d8d8;
  }
  * { box-sizing: border-box; margin: 0; padding: 0; }
  html, body { width: 841px; height: 1200px; overflow: hidden; background: #ececec; }
  .flyer {
    position: relative; width: 841px; height: 1200px; overflow: hidden;
    background: var(--light); font-family: "Open Sans", Arial, sans-serif; color: var(--grey-text);
  }

  /* Header */
  .header { position: absolute; left: 0; top: 0; width: 841px; height: 220px; }
  .header-accent { position: absolute; right: 0; top: 0; }
  .brand { position: absolute; left: 60px; top: 70px; display: flex; align-items: center; gap: 18px; }
  .brand-mark { width: 34px; height: 34px; background: var(--orange); }
  .brand-name { font-family: "Open Sans", Arial, sans-serif; font-weight: 600; font-size: 34px; color: var(--charcoal); letter-spacing: 0.5px; }

  /* Hero */
  .hero { position: absolute; left: 0; top: 220px; width: 841px; height: 480px; background: linear-gradient(90deg, var(--charcoal-deep) 0%, var(--charcoal) 100%); }
  .hero-photo {
    position: absolute; left: 380px; top: 0; width: 461px; height: 480px;
    background: linear-gradient(180deg, #4a4643 0%, #35322f 55%, #24211f 100%);
  }
  .hero-title {
    position: absolute; left: 60px; top: 60px;
    font-family: "Oswald", "Arial Narrow", sans-serif; font-weight: 700; text-transform: uppercase;
    font-size: 78px; line-height: 0.98; color: var(--light);
  }
  .hero-title .accent { color: var(--orange); }
  .call-bar {
    position: absolute; left: 0; top: 395px; width: 420px; height: 66px; background: var(--orange);
    display: flex; align-items: center; gap: 14px; padding-left: 60px;
    color: var(--light); font-weight: 700; font-size: 26px;
  }
  .call-bar svg { width: 26px; height: 26px; }

  /* Services */
  .services { position: absolute; left: 60px; top: 735px; width: 390px; }
  .section-title { font-family: "Oswald", "Arial Narrow", sans-serif; font-weight: 500; font-size: 24px; color: var(--charcoal); letter-spacing: 1px; }
  .section-rule { height: 2px; background: var(--rule); margin: 10px 0 22px; }
  .service-grid { display: grid; grid-template-columns: 1fr 1fr; row-gap: 26px; column-gap: 20px; }
  .service { display: flex; align-items: center; gap: 14px; font-weight: 700; font-size: 22px; color: var(--charcoal); }
  .service.wide { grid-column: 1 / 3; }
  .service-icon { width: 48px; height: 48px; border: 3px solid var(--orange); border-radius: 6px; background: #fff3e6; flex-shrink: 0; }

  /* About */
  .about { position: absolute; left: 490px; top: 735px; width: 300px; }
  .about-copy { font-size: 12.5px; line-height: 1.6; text-align: justify; }

  /* Contact box */
  .web-box {
    position: absolute; left: 520px; top: 1000px; width: 321px; height: 80px; background: var(--orange);
    padding: 14px 0 0 50px; color: var(--light); font-size: 14px; font-weight: 600; line-height: 1.8;
  }

  /* Footer */
  .footer { position: absolute; left: 0; top: 1080px; width: 841px; height: 120px; background: var(--charcoal); }
  .footer-accent { position: absolute; right: 0; top: 0; }
  .address { position: absolute; left: 60px; top: 34px; display: flex; gap: 16px; align-items: flex-start; color: var(--light); font-size: 15px; line-height: 1.6; }
  .address svg { width: 24px; height: 32px; margin-top: 4px; }
</style>
</head>
<body>
<div class="flyer">

  <header class="header">
    <svg class="header-accent" width="300" height="16" viewBox="0 0 300 16"><polygon points="20,0 300,0 300,16 0,16" fill="var(--orange)"/></svg>
    <div class="brand">
      <span class="brand-mark"></span>
      <span class="brand-name">Saltmarsh Valley Lending</span>
    </div>
  </header>

  <section class="hero">
    <div class="hero-photo" role="img" aria-label="Portrait of a smiling finance broker in a dark suit with arms folded"></div>
    <h1 class="hero-title">Saltmarsh<br><span class="accent">Valley</span><br>Lending</h1>
    <div class="call-bar">
      <span>Call:</span>
      <svg viewBox="0 0 24 24"><path d="M6.6 10.8a15.1 15.1 0 0 0 6.6 6.6l2.2-2.2a1 1 0 0 1 1-.25 11.4 11.4 0 0 0 3.6.57 1 1 0 0 1 1 1V20a1 1 0 0 1-1 1A17 17 0 0 1 3 4a1 1 0 0 1 1-1h3.5a1 1 0 0 1 1 1c0 1.25.2 2.45.57 3.57a1 1 0 0 1-.25 1z" fill="var(--light)"/></svg>
      <span>08 5550 1927</span>
    </div>
  </section>

  <section class="services">
    <h2 class="section-title">OUR SERVICES...</h2>
    <div class="section-rule"></div>
    <div class="service-grid">
      <div class="service"><span class="service-icon" role="img" aria-label="Car icon"></span>Car</div>
      <div class="service"><span class="service-icon" role="img" aria-label="4x4 vehicle icon"></span>4x4</div>
      <div class="service"><span class="service-icon" role="img" aria-label="Boat icon"></span>Boat</div>
      <div class="service"><span class="service-icon" role="img" aria-label="Excavator icon"></span>Excavator</div>
      <div class="service wide"><span class="service-icon" role="img" aria-label="Cash and house icon"></span>Cash Loans and houses</div>
    </div>
  </section>

  <section class="about">
    <h2 class="section-title">ABOUT US...</h2>
    <div class="section-rule"></div>
    <p class="about-copy">Saltmarsh Valley Lending is a locally owned finance broker helping families, farmers and small businesses across the region. We compare a wide panel of lenders to find the loan that suits your needs and budget. Whether you are buying a new car, a boat for the weekend, machinery for work or your first home, our friendly team makes the process simple, fast and personal. Call in for a chat and let us do the legwork for you.</p>
  </section>

  <div class="web-box">
    <div>info@saltmarshvalley.com.au</div>
    <div>www.saltmarshvalley.com.au</div>
  </div>

  <footer class="footer">
    <svg class="footer-accent" width="360" height="120" viewBox="0 0 360 120"><polygon points="40,0 360,0 360,120 0,120" fill="var(--orange)"/></svg>
    <div class="address">
      <svg viewBox="0 0 24 32"><path d="M12 0a11 11 0 0 0-11 11c0 8 11 21 11 21s11-13 11-21A11 11 0 0 0 12 0zm0 15a4 4 0 1 1 0-8 4 4 0 0 1 0 8z" fill="var(--orange)"/></svg>
      <div>Unit 4, 27 Harbourline Road<br>Saltmarsh QV 0830</div>
    </div>
  </footer>

</div>
</body>
</html>
```